Corvena Hotel, city center modern minimal hotel operating all year round, on Rhodes island Greece

city, modern ,all year operating hotel

Target Market(s)

tourists, business agents

Industry/Entity Type

tourism

Coding

Coded - Design and coding required

Number of Pages Required

2 page

Requirements
Must have
• room type photos and descriptions, amenities individual listing (graphic), comments sections, map driving location details
Nice to have
• gallery section, modern and minimal design, amenities section, individual room type descriptions, photos and facilities

```html
<!DOCTYPE html>
<html lang="en">
<head>
<meta charset="utf-8">
<title>Corvena Hotel – Explore Rhodes</title>
<link rel="stylesheet" href="https://fonts.googleapis.com/css2?family=DM+Serif+Display&family=Mulish:wght@400;600;700;800&display=swap">
<style>
:root{
  --gold:#c4962f;
  --gold-dark:#a97d1f;
  --green:#1f5a3e;
  --ink:#222222;
  --text:#4a4a4a;
  --muted:#8a8a8a;
  --line:#dcdcdc;
  --panel:#f2f2f4;
  --white:#ffffff;
  --footer:#1b1b1b;
}
*{box-sizing:border-box;margin:0;padding:0}
html,body{width:1200px;height:4587px;overflow:hidden}
body{font-family:"Mulish",sans-serif;color:var(--text);background:var(--white);position:relative}
.abs{position:absolute}
.serif{font-family:"DM Serif Display",serif}

/* header */
.site-header{position:absolute;left:0;top:0;width:1200px;height:116px;background:var(--white)}
.brand{position:absolute;left:135px;top:30px;display:flex;align-items:center;gap:14px}
.brand-mark{width:40px;height:40px;background:var(--green)}
.brand-name{font-family:"DM Serif Display",serif;font-size:34px;color:var(--gold);letter-spacing:1px}
.btn{display:inline-block;background:var(--gold);color:var(--white);font-family:"DM Serif Display",serif;font-size:15px;text-align:center}
.head-btn{position:absolute;top:21px;height:34px;line-height:34px}
.main-nav{position:absolute;top:73px;left:739px;font-family:"DM Serif Display",serif;font-size:16px;color:var(--ink)}
.main-nav span{position:absolute;white-space:nowrap}
.main-nav .active{color:var(--gold);border-bottom:2px solid var(--gold);padding-bottom:2px}

/* hero */
.hero{position:absolute;left:0;top:116px;width:1200px;height:516px;overflow:hidden}
.hero-photo{position:absolute;inset:0;background:linear-gradient(120deg,#4a2b14 0%,#8c5a2c 35%,#c8a16c 60%,#9a6a3a 80%,#5b3819 100%)}
.hero-shade{position:absolute;inset:0;background:rgba(0,0,0,.18)}
.hero-arrow{position:absolute;top:240px;width:38px;height:38px;border-radius:50%;background:var(--green)}
.hero-kicker{position:absolute;top:272px;left:0;width:1200px;text-align:center;color:var(--white);font-size:24px}
.hero-kicker:before{content:"";display:block;width:156px;height:2px;background:var(--white);margin:0 auto 10px}
.hero-title{position:absolute;top:320px;left:0;width:1200px;text-align:center;color:var(--white);font-size:64px;text-shadow:0 2px 6px rgba(0,0,0,.35)}
.hero-curve{position:absolute;left:0;bottom:0;width:1200px;height:120px}

/* booking */
.booking{position:absolute;left:132px;top:555px;width:936px;height:166px;background:var(--white);box-shadow:0 6px 24px rgba(0,0,0,.12)}
.field{position:absolute;height:45px;border:1px solid var(--line);font-size:10px;color:#666;padding-left:16px;line-height:43px;letter-spacing:.3px}
.field svg{position:absolute;right:12px;top:15px}
.book-btn{position:absolute;left:473px;top:90px;width:438px;height:46px;line-height:46px;font-size:19px}

/* section headings */
.sec-title{position:absolute;left:0;width:1200px;text-align:center;font-family:"DM Serif Display",serif;font-size:26px;color:var(--ink)}
.sec-title:after{content:"";display:block;width:32px;height:2px;background:var(--ink);margin:14px auto 0}

/* amenities */
.amenity{position:absolute;text-align:center;font-size:13px;color:var(--ink);line-height:1.6}
.amenity svg{display:block;margin:0 auto 14px}
.col-rule{position:absolute;top:858px;width:1px;height:308px;background:var(--line)}

/* rooms */
.rooms{position:absolute;left:0;top:1220px;width:1200px;height:904px;background:var(--panel)}
.room{position:absolute;width:298px;height:358px;background:var(--panel);border:1px solid var(--line);text-align:center}
.room-photo{height:178px}
.room h3{font-size:12.5px;font-weight:600;color:var(--ink);letter-spacing:.4px;margin:30px 0 14px}
.room p{font-size:10.5px;line-height:1.45;padding:0 38px;color:var(--text);height:58px}
.room .more{display:inline-block;background:var(--gold);color:var(--white);font-size:9.5px;font-weight:800;padding:5px 11px;letter-spacing:.3px}
.room.featured{background:var(--gold);border-color:var(--gold)}
.room.featured h3,.room.featured p{color:var(--white)}
.room.featured .more{background:var(--white);color:var(--gold)}

/* testimonials */
.review{position:absolute;top:2265px;width:290px;height:349px;background:var(--white);box-shadow:0 4px 18px rgba(0,0,0,.08);text-align:center;padding:34px 28px 0}
.quote{font-family:"DM Serif Display",serif;font-size:54px;color:var(--gold);line-height:40px;height:36px}
.review h4{font-size:12px;font-weight:800;color:var(--ink);margin:16px 0 18px;letter-spacing:.3px}
.review p{font-size:12px;line-height:1.55;color:var(--text);height:190px}
.review .who{font-size:12px;font-weight:700;color:var(--ink)}
.chev{position:absolute;top:2430px}

/* gallery */
.shot{position:absolute;width:225px;height:181px}
.view-all{position:absolute;left:540px;top:3197px;width:120px;height:29px;line-height:29px;background:var(--gold);color:var(--white);font-size:10px;font-weight:800;text-align:center;letter-spacing:.4px}

/* about */
.badge{position:absolute;background:#f7f7f7;border:3px solid #1e2f6b}
.about-rule{position:absolute;left:527px;top:3300px;width:1px;height:420px;background:var(--line)}
.about-text{position:absolute;left:609px;top:3330px;width:431px;font-size:12px;line-height:1.52;color:var(--text);text-align:justify}
.about-text p{margin-bottom:15px}

/* map */
.map{position:absolute;left:0;top:3783px;width:1200px;height:450px;background:linear-gradient(180deg,#e9edf2 0%,#f4f5f7 55%,#ffffff 100%)}

/* footer */
.site-footer{position:absolute;left:0;top:4233px;width:1200px;height:354px;background:linear-gradient(180deg,#1f1f1f,#151515);color:var(--white)}
.foot-brand{position:absolute;left:135px;top:100px;display:flex;align-items:center;gap:14px}
.foot-brand .brand-mark{width:46px;height:46px;background:var(--gold)}
.foot-brand .brand-name{font-size:30px;color:var(--white)}
.foot-h{position:absolute;top:48px;font-size:12px;font-weight:800;letter-spacing:.6px}
.foot-item{position:absolute;font-size:11px;line-height:1.45;display:flex;gap:12px;align-items:flex-start}
.foot-item .dot{width:22px;height:22px;border-radius:50%;background:var(--white);flex:none;display:flex;align-items:center;justify-content:center}
.foot-menu{position:absolute;left:731px;top:84px;font-size:11px;line-height:24px;letter-spacing:.3px}
.copyright{position:absolute;left:0;top:4537px;width:1200px;text-align:center;font-size:10px;color:#cfcfcf}
</style>
</head>
<body>

<header class="site-header">
  <div class="brand"><span class="brand-mark"></span><span class="brand-name">Corvena Hotel</span></div>
  <a class="btn head-btn" style="left:739px;width:124px">Book Now</a>
  <a class="btn head-btn" style="left:908px;width:160px">Hotel With Flight</a>
  <nav class="main-nav">
    <span class="active" style="left:0">Home</span>
    <span style="left:80px">Rooms</span>
    <span style="left:174px">Gallery</span>
    <span style="left:272px">Contact</span>
  </nav>
</header>

<section class="hero">
  <div class="hero-photo" role="img" aria-label="Hotel reception lobby with wooden counter and warm lighting"></div>
  <div class="hero-shade"></div>
  <span class="hero-arrow" style="left:60px"><svg width="38" height="38" viewBox="0 0 38 38"><path d="M22 12l-7 7 7 7" stroke="#fff" stroke-width="2.5" fill="none"/></svg></span>
  <span class="hero-arrow" style="left:1100px"><svg width="38" height="38" viewBox="0 0 38 38"><path d="M16 12l7 7-7 7" stroke="#fff" stroke-width="2.5" fill="none"/></svg></span>
  <div class="hero-kicker serif">Relax &amp; Enjoy</div>
  <h1 class="hero-title serif">Explore Rhodes</h1>
  <svg class="hero-curve" viewBox="0 0 1200 120" preserveAspectRatio="none">
    <path d="M0 60 Q600 -10 1200 60 L1200 120 L0 120Z" fill="#fff"/>
    <path d="M0 60 Q600 -10 1200 60" stroke="#c4962f" stroke-width="4" fill="none"/>
  </svg>
</section>

<form class="booking">
  <div class="field" style="left:25px;top:27px;width:216px">FULL NAME*</div>
  <div class="field" style="left:247px;top:27px;width:216px">EMAIL*</div>
  <div class="field" style="left:471px;top:27px;width:216px">ARRIVAL DATE*
    <svg width="14" height="14" viewBox="0 0 14 14"><rect x="1" y="2" width="12" height="11" fill="none" stroke="#777"/><path d="M1 5h12M4 8h2M8 8h2M4 10h2M8 10h2" stroke="#777"/></svg></div>
  <div class="field" style="left:696px;top:27px;width:215px">DEPARTURE DATE*
    <svg width="14" height="14" viewBox="0 0 14 14"><rect x="1" y="2" width="12" height="11" fill="none" stroke="#777"/><path d="M1 5h12M4 8h2M8 8h2M4 10h2M8 10h2" stroke="#777"/></svg></div>
  <div class="field" style="left:25px;top:90px;width:213px">ROOMS*
    <svg width="10" height="10" viewBox="0 0 10 10"><path d="M2 3l3 3 3-3" stroke="#444" stroke-width="1.5" fill="none"/></svg></div>
  <div class="field" style="left:249px;top:90px;width:100px">ADULTS*
    <svg width="10" height="10" viewBox="0 0 10 10"><path d="M2 3l3 3 3-3" stroke="#444" stroke-width="1.5" fill="none"/></svg></div>
  <div class="field" style="left:365px;top:90px;width:96px">CHILDREN
    <svg width="10" height="10" viewBox="0 0 10 10"><path d="M2 3l3 3 3-3" stroke="#444" stroke-width="1.5" fill="none"/></svg></div>
  <a class="btn book-btn">Book Now</a>
</form>

<h2 class="sec-title" style="top:764px">Amenities</h2>
<span class="col-rule" style="left:335px"></span>
<span class="col-rule" style="left:566px"></span>
<span class="col-rule" style="left:848px"></span>

<div class="amenity" style="left:132px;top:888px;width:203px">
  <svg width="50" height="48" viewBox="0 0 50 48"><rect x="4" y="12" width="42" height="28" fill="none" stroke="#1f5a3e" stroke-width="3"/><rect x="10" y="18" width="14" height="10" fill="#1f5a3e"/><path d="M28 20h12M28 26h10M18 4l7 7 7-7M14 44h22" stroke="#1f5a3e" stroke-width="2.5" fill="none"/></svg>
  Satellite Television Set</div>
<div class="amenity" style="left:335px;top:888px;width:231px">
  <svg width="50" height="48" viewBox="0 0 50 48"><rect x="10" y="4" width="30" height="40" fill="none" stroke="#1f5a3e" stroke-width="3"/><rect x="16" y="14" width="6" height="20" fill="#1f5a3e"/><rect x="27" y="14" width="6" height="20" fill="#1f5a3e"/></svg>
  Mini Bar</div>
<div class="amenity" style="left:566px;top:888px;width:282px">
  <svg width="50" height="48" viewBox="0 0 50 48"><rect x="10" y="6" width="24" height="14" rx="7" fill="#1f5a3e"/><path d="M20 20v18M34 10h8M34 16h8" stroke="#1f5a3e" stroke-width="4"/><path d="M20 38q8 6 12-2" stroke="#1f5a3e" stroke-width="2" fill="none"/></svg>
  Hairdryer</div>
<div class="amenity" style="left:848px;top:888px;width:220px">
  <svg width="50" height="48" viewBox="0 0 50 48"><rect x="6" y="4" width="40" height="40" fill="none" stroke="#1f5a3e" stroke-width="3"/><path d="M6 4l40 40M26 4l20 20M6 24l20 20M46 4L6 44M26 4L6 24M46 24L26 44" stroke="#1f5a3e" stroke-width="4"/></svg>
  Laminated Flooring</div>

<div class="amenity" style="left:132px;top:1040px;width:203px">
  <svg width="50" height="48" viewBox="0 0 50 48"><path d="M4 18h42v8q0 12-12 12H16Q4 38 4 26z" fill="#1f5a3e"/><path d="M8 18V6h8M14 38l-3 6M36 38l3 6" stroke="#1f5a3e" stroke-width="3" fill="none"/></svg>
  En sure bathroom<br>with amenities</div>
<div class="amenity" style="left:335px;top:1040px;width:231px">
  <svg width="50" height="48" viewBox="0 0 50 48"><path d="M8 18a16 14 0 0 1 32 0z" fill="#1f5a3e"/><path d="M24 18v14M10 32h28l6 10M14 32l-4 10" stroke="#1f5a3e" stroke-width="3" fill="none"/></svg>
  Lounge sun<br>deck area</div>
<div class="amenity" style="left:566px;top:1040px;width:282px">
  <svg width="50" height="48" viewBox="0 0 50 48"><rect x="12" y="4" width="26" height="22" fill="none" stroke="#1f5a3e" stroke-width="3"/><path d="M25 4v22M12 15h26M6 28h38M8 28v16M42 28v16M15 32v12M21 32v12M27 32v12M33 32v12M6 44h38" stroke="#1f5a3e" stroke-width="2.5"/></svg>
  Double glazed<br>windows and balcony</div>
<div class="amenity" style="left:848px;top:1040px;width:220px">
  <svg width="50" height="48" viewBox="0 0 50 48"><rect x="8" y="4" width="34" height="38" fill="#1f5a3e"/><rect x="14" y="10" width="22" height="24" fill="none" stroke="#fff" stroke-width="2"/><circle cx="25" cy="22" r="5" fill="none" stroke="#fff" stroke-width="2"/><path d="M12 42v4M38 42v4" stroke="#1f5a3e" stroke-width="3"/></svg>
  Safe storage<br>area for valuables</div>

<section class="rooms">
  <h2 class="sec-title" style="top:32px">Rooms</h2>

  <article class="room" style="left:132px;top:120px">
    <div class="room-photo" role="img" aria-label="Apartment living area with warm wall lights" style="background:linear-gradient(135deg,#3a2a10,#8a6a28 50%,#d8c08a)"></div>
    <h3>APARTMENT FOR 4 ADULTS</h3>
    <p>Situated on the top floor of the hotel, this fully air-conditioned apartment consists of 2 bedrooms, living room, kitchen and wooden patio.</p>
    <span class="more">READ MORE</span>
  </article>
  <article class="room featured" style="left:447px;top:120px">
    <div class="room-photo" role="img" aria-label="Superior double room with striped bedspread" style="background:linear-gradient(135deg,#2c2116,#6d5238 50%,#d3c2a6)"></div>
    <h3>SUPERIOR DOUBLE ROOM</h3>
    <p>This spacious room features a queen size bed or a sofa that turns into a double bed. It features satellite television, a coffee machine and other amenities.</p>
    <span class="more">READ MORE</span>
  </article>
  <article class="room" style="left:767px;top:120px">
    <div class="room-photo" role="img" aria-label="Quadruple room with large bed and window" style="background:linear-gradient(135deg,#5a3c22,#a27850 50%,#e2d2bc)"></div>
    <h3>QUADRUPLE ROOM</h3>
    <p>This more spacious room has a queen size bed and a sofa that turns into a double bed. It features satellite TV, a coffee machine and other amenities.</p>
    <span class="more">READ MORE</span>
  </article>

  <article class="room" style="left:132px;top:502px">
    <div class="room-photo" role="img" aria-label="Triple room with twin beds and lamps" style="background:linear-gradient(135deg,#2a1e12,#7a5a30 50%,#cdb88a)"></div>
    <h3>TRIPLE ROOM</h3>
    <p>The room features a twin beds and extra foldaway single bed, private bathroom with bathtub and other amenities. The balcony faces the street.</p>
    <span class="more">READ MORE</span>
  </article>
  <article class="room" style="left:447px;top:502px">
    <div class="room-photo" role="img" aria-label="Single room with bed and wardrobe" style="background:linear-gradient(135deg,#3e2e1a,#8f7048 50%,#d9c8a8)"></div>
    <h3>SINGLE ROOM</h3>
    <p>This comfortable room features a balcony, laminated floors, private bathroom with shower, office desk, satellite TV and other amenities.</p>
    <span class="more">READ MORE</span>
  </article>
  <article class="room" style="left:767px;top:502px">
    <div class="room-photo" role="img" aria-label="Double room with dark patterned bedspread" style="background:linear-gradient(135deg,#241a10,#6e4e2c 50%,#c9b08a)"></div>
    <h3>DOUBLE ROOM</h3>
    <p>Comfortable room features a balcony, laminated floors, private bathroom, office desk, satellite TV and other amenities.</p>
    <span class="more">READ MORE</span>
  </article>
</section>

<h2 class="sec-title" style="top:2168px">Testimonails</h2>
<svg class="chev" style="left:64px" width="20" height="34" viewBox="0 0 20 34"><path d="M17 2L3 17l14 15" stroke="#888" stroke-width="2" fill="none"/></svg>
<svg class="chev" style="left:1118px" width="20" height="34" viewBox="0 0 20 34"><path d="M3 2l14 15L3 32" stroke="#888" stroke-width="2" fill="none"/></svg>

<article class="review" style="left:132px">
  <div class="quote">&ldquo;</div>
  <h4>SUPERB</h4>
  <p>Stavros Welcomed us with a very generous touch, Authentic Greek Hospitality. If you want to experience a genuine village experience with the community, and savor the magnificent viewing in the streets, like postal cards, well this is the right place away from the touristic crowd, I loved it!!</p>
  <div class="who">Alain Moreau</div>
</article>
<article class="review" style="left:456px">
  <div class="quote">&ldquo;</div>
  <h4>EXCEPTIONAL</h4>
  <p>The location fo the place was pretty close to the old town, the beach, bars, and restaurants, facilities were really good and staff was very friendly and kind ti help in any situation</p>
  <div class="who">Alain Moreau</div>
</article>
<article class="review" style="left:780px">
  <div class="quote">&ldquo;</div>
  <h4>PERFECT LOCATION</h4>
  <p>The Corvena is a charming little place in a perfect spot. Rooms are comfortable, very effective AC and a compact, but very good, bathroom. Cleaning staff v good. Breakfast was a very good selection and lovely location to eat on the patio. Staff were friendly and helpful all round. Would definitely return!</p>
  <div class="who">Alain Moreau</div>
</article>

<section style="position:absolute;left:0;top:2680px;width:1200px;height:587px;background:var(--panel)">
  <h2 class="sec-title" style="top:32px">Gallery</h2>
</section>
<div class="shot" role="img" aria-label="Reception desk with framed pictures" style="left:132px;top:2792px;background:linear-gradient(135deg,#3a2412,#9a6a38)"></div>
<div class="shot" role="img" aria-label="Bedroom with patterned bedspread" style="left:369px;top:2792px;background:linear-gradient(135deg,#6a5030,#d8c6a4)"></div>
<div class="shot" role="img" aria-label="Double bed with decorative wall panel" style="left:605px;top:2792px;background:linear-gradient(135deg,#2a1e16,#8a6a4a)"></div>
<div class="shot" role="img" aria-label="Group of guests holding certificates" style="left:840px;top:2792px;background:linear-gradient(135deg,#4a3a30,#a48a70)"></div>
<div class="shot" role="img" aria-label="Room with balcony doors and curtains" style="left:132px;top:2986px;background:linear-gradient(135deg,#2e2820,#8a7a62)"></div>
<div class="shot" role="img" aria-label="Desk and chair by the window" style="left:369px;top:2986px;background:linear-gradient(135deg,#6a4a24,#c8a66a)"></div>
<div class="shot" role="img" aria-label="Bathroom shower with glass screen" style="left:605px;top:2986px;background:linear-gradient(135deg,#c8c4bc,#f2efe8)"></div>
<div class="shot" role="img" aria-label="Television on wooden cabinet" style="left:840px;top:2986px;background:linear-gradient(135deg,#5a3a1a,#c89a5a)"></div>
<a class="view-all">VIEW ALL IMAGES</a>

<span class="badge" style="left:142px;top:3316px;width:143px;height:132px"></span>
<span class="badge" style="left:299px;top:3316px;width:142px;height:132px"></span>
<span class="badge" style="left:142px;top:3466px;width:143px;height:132px"></span>
<span class="abs" style="left:346px;top:3486px;width:60px;height:60px;border-radius:50%;background:#e6e6e6"></span>
<span class="abs" style="left:318px;top:3560px;width:120px;height:26px;background:#f3dcdc"></span>
<span class="abs" style="left:196px;top:3631px;width:89px;height:89px;background:#1e2f6b"></span>
<span class="abs" style="left:306px;top:3631px;width:78px;height:89px;background:#eef4fa;border:1px solid #d6e2ee"></span>
<span class="about-rule"></span>
<div class="about-text">
  <p>Situated at the very heart of Rhodes town, the hotel provides easy access to all major points of interest all within walking distance.</p>
  <p>The hotel is renowned in the local market due to its operation which “runs” 365 days a year. All rooms have been renovated recently and offer a unique design with modern furnishes. Being in constant operation for the last 47 years, and gone through numerous renovations the hotel operates mainly with repeaters who value and appreciate its comfort, cleanliness, friendly attitude, amenities and personality just to name a few.</p>
  <p>On line booking is available through mainstream agencies or directly with the hotel, with its own platform at www.corvenahotel.com were various offers are available all through the year.</p>
  <p>Our reception operates 24 hours and 7 days a week, making check in or providing information a breeze. All the information one might need for sightseeing the island either by boat, bike, car or motorbike is available there. Tickets for shows, boat trips or museums are also available, as well as car hire from the hotels own rental company, offering lower rates than any competitor local or otherwise.</p>
</div>

<div class="map" role="img" aria-label="Street map of Rhodes town showing the hotel location">
  <svg class="abs" style="left:556px;top:160px" width="22" height="30" viewBox="0 0 22 30"><path d="M11 29C4 18 1 14 1 10a10 10 0 0 1 20 0c0 4-3 8-10 19z" fill="#d23b3b"/><circle cx="11" cy="10" r="4" fill="#fff"/></svg>
</div>

<footer class="site-footer">
  <div class="foot-brand"><span class="brand-mark"></span><span class="brand-name">Corvena Hotel</span></div>

  <div class="foot-h" style="left:429px">CONTACT US</div>
  <div class="foot-item" style="left:429px;top:84px"><span class="dot"><svg width="10" height="12" viewBox="0 0 10 12"><path d="M5 12C1 7 0 5 0 4a5 4 0 0 1 10 0c0 1-1 3-5 8z" fill="#1b1b1b"/></svg></span><span>25 Odos Thalassis 12,<br>Rhodes 851 00</span></div>
  <div class="foot-item" style="left:429px;top:136px"><span class="dot"><svg width="10" height="10" viewBox="0 0 10 10"><path d="M1 1h3l1 3-2 1q1 2 3 3l1-2 3 1v3Q4 10 1 1z" fill="#1b1b1b"/></svg></span><span>Call Us<br>(+30) 2241055410-1</span></div>
  <div class="foot-item" style="left:429px;top:188px"><span class="dot"><svg width="11" height="8" viewBox="0 0 11 8"><rect width="11" height="8" fill="#1b1b1b"/><path d="M0 0l5.5 4L11 0" stroke="#fff" fill="none"/></svg></span><span>E mail Us<br>info@corvenahotel.gr</span></div>

  <div class="foot-h" style="left:731px">MENU</div>
  <div class="foot-menu">HOME<br>ROOMS<br>GALLERY<br>CONTACT US</div>

  <div class="foot-h" style="left:961px">FOLLOW US</div>
  <div class="foot-item" style="left:961px;top:96px"><span class="dot"></span><span>Like us on<br>FRIENDLY</span></div>
  <div class="foot-item" style="left:961px;top:148px"><span class="dot"></span><span>Follow us on<br>CHIRPER</span></div>
  <div class="foot-item" style="left:961px;top:200px"><span class="dot"></span><span>Follow us on<br>WORKLINK</span></div>
</footer>
<div class="copyright">Copyright © 2022 All Rights Reserved</div>

</body>
</html>
```